Webdesign für Gemeinschaftspraxis (13820)
Zielgruppe
Die Website ist für eine fachärztliche Gemeinschaftspraxis, die sich aus Internisten, Betriebsmedizinern, Präventionsärzten, Kardiologen, Allgemeinmedizinern und Phlebologen zusammensetzt.
Die Zielgruppe sind bestehende Patienten sowie potentielle Patienten.
Die Website soll informativ sein.
Aufgabenstellung
Die Website soll in schlichten Farben gehalten sein, die zum Logo und zu den Fotos passen.
Die Website soll als kurzer, informativer Auftritt dienen
Die gelieferten Fotos sollen verwendet werden.
Es soll eine Onepage-Website werden, die so aufgebaut ist, wie die Website unter dem folgenden Link: https://www.kolbenfeld-portal.de/

```html
<!DOCTYPE html>
<html lang="de">
<head>
<meta charset="utf-8">
<title>Gemeinschaftspraxis Ahrental</title>
<link href="https://fonts.googleapis.com/css2?family=Karla:ital,wght@0,400;0,500;0,700;1,400&display=swap" rel="stylesheet">
<style>
:root{
  --navy:#1a2a5c;
  --navy-soft:#3a4f8f;
  --blue:#3550b4;
  --corner:#c6cce0;
  --ink:#1d2a52;
  --text:#6a6f7d;
  --light:#f7f7f9;
  --row:#eeeeef;
  --btn:#7f9bcb;
}
*{box-sizing:border-box;margin:0;padding:0}
html,body{width:1200px;height:3873px;overflow:hidden}
body{font-family:'Karla',sans-serif;color:var(--ink);background:#fff;position:relative}

/* hero */
.hero{position:absolute;left:0;top:0;width:1200px;height:630px;overflow:hidden}
.hero-photo{position:absolute;inset:0;background:linear-gradient(160deg,#f4f3f1 0%,#e9e5de 40%,#cfb48c 70%,#e7e3dc 100%)}
.hero svg.shapes{position:absolute;left:0;top:0}
.logo{position:absolute;left:111px;top:0;width:232px;height:150px;background:#fff;display:flex;flex-direction:column;align-items:center;justify-content:center;gap:8px}
.logo-mark{width:14px;height:14px;background:var(--navy)}
.logo-name{font-weight:700;font-size:15px;color:var(--navy);letter-spacing:.5px;text-align:center;line-height:1.3}
.nav{position:absolute;left:471px;top:27px;width:729px;height:57px;background:var(--navy);display:flex;align-items:center;gap:32px;padding-left:68px}
.nav a{color:#fff;font-size:12px;font-weight:700;letter-spacing:.5px;text-decoration:none}
.hero-title{position:absolute;right:110px;top:448px;text-align:right;background:rgba(255,255,255,.45);padding:4px 0 6px 20px}
.hero-title h1{font-size:42px;font-weight:700;color:var(--navy);letter-spacing:1px;line-height:1}
.hero-title p{font-size:31px;color:var(--navy);letter-spacing:1.5px;line-height:1.15}

.sec-title{position:absolute;left:0;width:1200px;text-align:center;font-size:31px;font-weight:400;letter-spacing:2px;color:var(--ink)}

/* services */
.services{position:absolute;left:0;top:632px;width:1200px;height:744px;background:var(--light)}
.services .lead{position:absolute;left:0;top:124px;width:1200px;text-align:center;font-style:italic;font-size:15px;line-height:22px;color:#555}
.card{position:absolute;width:224px;height:188px;background:#fff;box-shadow:0 2px 8px rgba(0,0,0,.08);display:flex;flex-direction:column;align-items:center;justify-content:center;text-align:center;font-size:16px;font-weight:700;letter-spacing:.8px;line-height:26px;color:var(--ink);overflow:hidden}
.card svg{position:absolute;left:0;top:0}
.card span{position:relative;z-index:1}
.card.active{background:var(--navy-soft);color:#fff}
.card.active span.label{text-decoration:underline}
.card .more{position:relative;z-index:1;margin-top:18px;border:1px solid #fff;font-size:10px;letter-spacing:.8px;padding:2px 8px;line-height:18px}
.dots{position:absolute;left:577px;top:648px;display:flex;gap:10px}
.dots i{width:9px;height:9px;background:#8f9bbf;display:block}
.dots i.on{background:var(--navy)}

/* doctors */
.doc{position:absolute;top:1496px;width:309px;height:411px;background:#fff;box-shadow:0 2px 12px rgba(0,0,0,.08);text-align:center}
.doc .photo{width:135px;height:135px;margin:43px auto 0;border:1px solid #79a3c9;padding:3px;background:#fff}
.doc .photo div{width:100%;height:100%;background:linear-gradient(180deg,#9a9a9a,#c9b5a3)}
.doc h3{font-size:16px;font-weight:700;margin-top:22px;color:#333}
.doc .role{font-size:11px;color:#999;margin-top:4px}
.doc p{font-size:13px;line-height:22.5px;color:#666;margin:16px 32px 0}

/* hours */
.hours{position:absolute;left:0;top:1985px;width:1200px;height:903px;background:linear-gradient(100deg,#3a4f82 0%,#5a5f78 30%,#4e6396 60%,#8a4a2c 85%,#b5723a 100%)}
.hours .sec-title{color:#fff;top:55px}
.table{position:absolute;left:111px;top:99px;width:978px;border-collapse:collapse;font-size:14px}
.table th{background:var(--blue);color:#fff;text-align:left;font-size:13px;letter-spacing:.5px;height:40px;padding-left:16px}
.table td{height:64.5px;vertical-align:top;padding:18px 0 0 16px;line-height:19px;color:#333;border-right:1px solid #ddd;width:161px}
.table td:last-child{border-right:none}
.table tr:nth-child(even) td{background:var(--row)}
.table tr:nth-child(odd) td{background:#fff}

/* team */
.team-photo{position:absolute;left:112px;top:3000px;width:395px;height:520px;z-index:0;
  background:linear-gradient(180deg,#f2f4f9 0%,#d8c0aa 20%,#c89e80 40%,#2a58b8 58%,#1d3f92 100%);
  border-radius:190px 190px 0 0}
.team-title{position:absolute;left:531px;top:2980px;font-size:31px;letter-spacing:1.5px;color:var(--ink);z-index:2;line-height:40px}
.team-line{position:absolute;left:798px;top:2998px;width:206px;height:1px;background:#ddd;z-index:2}
.team-line::before{content:"";position:absolute;left:-6px;top:-4px;width:9px;height:9px;border:1px solid #ddd;border-radius:50%;background:#fff}
.arrow{position:absolute;top:2984px;width:32px;height:31px;display:flex;align-items:center;justify-content:center;z-index:2}
.arrow.prev{left:1021px;background:var(--navy)}
.arrow.next{left:1055px;background:#e4e4e4}
.member{position:absolute;left:531px;top:3050px;width:558px;z-index:2}
.member h3{font-size:21px;font-weight:400;letter-spacing:1px;color:#333}
.member .pos{font-size:11px;font-style:italic;color:#777;margin-top:3px}
.member p{font-size:12.4px;line-height:22.5px;color:#666;margin-top:22px}
.member p:first-of-type{margin-top:28px}

/* footer */
.footer{position:absolute;left:0;top:3520px;width:1200px;height:353px;background:var(--navy);color:#7c90c4}
.footer h2{position:absolute;top:83px;font-size:29px;font-weight:400;letter-spacing:1.2px;color:#6d86c6}
.contact{position:absolute;font-size:12.5px;display:flex;align-items:center;gap:10px;color:#7c90c4}
.field{position:absolute;height:48px;background:#213673;border:1px solid #2c4184;font-size:12px;font-style:italic;color:#6f83bd;padding:16px 0 0 16px;letter-spacing:.5px}
.submit{position:absolute;left:612px;top:237px;width:475px;height:50px;background:var(--btn);color:var(--navy);text-align:center;line-height:50px;font-size:14px;letter-spacing:2px;font-weight:500}
</style>
</head>
<body>

<header class="hero">
  <div class="hero-photo" role="img" aria-label="Foto des hellen Empfangsbereichs der Praxis mit Holztresen"></div>
  <svg class="shapes" width="1200" height="630" viewBox="0 0 1200 630">
    <polygon points="0,0 700,0 0,180" fill="#fff"/>
    <polygon points="0,180 0,630 470,630" fill="#1a2a5c"/>
  </svg>
  <div class="logo">
    <div class="logo-mark"></div>
    <div class="logo-name">GEMEINSCHAFTSPRAXIS AHRENTAL</div>
  </div>
  <nav class="nav">
    <a>HOME</a><a>DIENSTLEISTUNGEN</a><a>UNSER TEAM</a><a>ÖFFNUNGSZEITEN</a><a>KONTAKTIERE UNS</a>
  </nav>
  <div class="hero-title">
    <h1>SED UT PERSPICIATIS</h1>
    <p>UNDE OMNIS ISTE NATUS</p>
  </div>
</header>

<section class="services">
  <h2 class="sec-title" style="top:78px">UNSERE DIENSTLEISTUNGEN</h2>
  <p class="lead">Nemo enim ipsam voluptatem quia voluptas sit aspernatur aut odit aut fugit, sed quia<br>consequuntur magni dolores eos qui ratione voluptatem sequi nesciunt.</p>

  <div class="card" style="left:120px;top:204px"><svg width="224" height="188"><polygon points="0,0 44,0 0,62" fill="#c6cce0"/><polygon points="224,110 224,188 168,188" fill="#c6cce0"/></svg><span>GESUNDHEITSVORSORGE<br>/PRÄVENTION/<br>GESUNDHEITS-CHECK-UP</span></div>
  <div class="card" style="left:362px;top:204px"><svg width="224" height="188"><polygon points="0,0 44,0 0,62" fill="#c6cce0"/><polygon points="224,110 224,188 168,188" fill="#c6cce0"/></svg><span>IMPFUNGEN UND<br>REISEIMPFUNGEN</span></div>
  <div class="card active" style="left:612px;top:204px"><svg width="224" height="188"><polygon points="0,0 44,0 0,62" fill="#fff"/><polygon points="224,110 224,188 168,188" fill="#fff"/></svg><span class="label">MÄNNERVORSORGE</span><span class="more">MEHR INFORMATIONEN</span></div>
  <div class="card" style="left:854px;top:204px"><svg width="224" height="188"><polygon points="0,0 44,0 0,62" fill="#c6cce0"/><polygon points="224,110 224,188 168,188" fill="#c6cce0"/></svg><span>DIABETES<br>MELLITUS</span></div>

  <div class="card" style="left:120px;top:418px"><svg width="224" height="188"><polygon points="0,0 44,0 0,62" fill="#c6cce0"/><polygon points="224,110 224,188 168,188" fill="#c6cce0"/></svg><span>PSYCHOSOMATISCHE<br>GRUNDVERSORGUNG</span></div>
  <div class="card" style="left:362px;top:418px"><svg width="224" height="188"><polygon points="0,0 44,0 0,62" fill="#c6cce0"/><polygon points="224,110 224,188 168,188" fill="#c6cce0"/></svg><span>KORONARE<br>HERZERKRANKUNG<br>(KHK)</span></div>
  <div class="card" style="left:612px;top:418px"><svg width="224" height="188"><polygon points="0,0 44,0 0,62" fill="#c6cce0"/><polygon points="224,110 224,188 168,188" fill="#c6cce0"/></svg><span>ASTHMA<br>BRONCHIAL</span></div>
  <div class="card" style="left:854px;top:418px"><svg width="224" height="188"><polygon points="0,0 44,0 0,62" fill="#c6cce0"/><polygon points="224,110 224,188 168,188" fill="#c6cce0"/></svg><span>PALLIATIVERSORGUNG</span></div>

  <div class="dots"><i></i><i class="on"></i><i></i></div>
</section>

<h2 class="sec-title" style="top:1432px">UNSERE ÄRZTE</h2>
<div class="doc" style="left:111px"><div class="photo"><div role="img" aria-label="Porträtfoto von Lena Harting"></div></div><h3>Lena Harting</h3><div class="role">Vice President</div><p>Neque porro quisquam est, qui dolorem ipsum quia dolor sit amet, consectetur, adipisci velit, sed quia non numquam eius modi tempora incidunt ut labore et dolore.</p></div>
<div class="doc" style="left:446px"><div class="photo"><div role="img" aria-label="Porträtfoto von Jonas.K"></div></div><h3>Jonas.K</h3><div class="role">Vice President</div><p>Neque porro quisquam est, qui dolorem ipsum quia dolor sit amet, consectetur, adipisci velit, sed quia non numquam eius modi tempora incidunt ut labore et dolore.</p></div>
<div class="doc" style="left:780px"><div class="photo"><div role="img" aria-label="Porträtfoto von Milo Brenner"></div></div><h3>Milo Brenner</h3><div class="role">Vice President</div><p>Neque porro quisquam est, qui dolorem ipsum quia dolor sit amet, consectetur, adipisci velit, sed quia non numquam eius modi tempora incidunt ut labore et dolore.</p></div>

<section class="hours" role="img" aria-label="Hintergrundfoto des Praxisgebäudes mit Herbstlaub">
  <h2 class="sec-title">ÖFFNUNGSZEITEN</h2>
  <table class="table">
    <tr><th>ZEIT</th><th>MONTAG</th><th>DIENSTAG</th><th>MITTWOCH</th><th>DONNERSTAG</th><th>FREITAG</th></tr>
    <tr><td>AB 7:30</td><td>Blutentnahme/<br>Ultraschall</td><td>Blutentnahme/<br>Ultraschall</td><td>Blutentnahme/<br>Ultraschall</td><td>Blutentnahme/<br>Ultraschall</td><td>Blutentnahme/<br>Ultraschall</td></tr>
    <tr><td>8:00-9:30</td><td>Freie<br>Sprechstunde</td><td>Freie<br>Sprechstunde</td><td>Freie<br>Sprechstunde</td><td>Freie<br>Sprechstunde</td><td>Freie<br>Sprechstunde</td></tr>
    <tr><td>9:00-10:00</td><td>Freie<br>Sprechstunde</td><td>Freie<br>Sprechstunde</td><td>Freie<br>Sprechstunde</td><td>Freie<br>Sprechstunde</td><td>Freie<br>Sprechstunde</td></tr>
    <tr><td>10:00-11:00</td><td>Freie<br>Sprechstunde</td><td>Freie<br>Sprechstunde</td><td>Freie<br>Sprechstunde</td><td>Freie<br>Sprechstunde</td><td>Freie<br>Sprechstunde</td></tr>
    <tr><td>11:00-12:00</td><td>Freie<br>Sprechstunde</td><td>Freie<br>Sprechstunde</td><td>Freie<br>Sprechstunde</td><td>Freie<br>Sprechstunde</td><td>Freie<br>Sprechstunde</td></tr>
    <tr><td>12:00-13:00</td><td>Hausbesuche</td><td>Hausbesuche</td><td>Hausbesuche</td><td>Hausbesuche</td><td>Hausbesuche</td></tr>
    <tr><td>13:00-14:00</td><td>Mittagspause</td><td>Mittagspause</td><td>Mittagspause</td><td>Mittagspause</td><td>Mittagspause</td></tr>
    <tr><td>14:00-15:30</td><td>Mittagspause</td><td>Mittagspause</td><td>Mittagspause</td><td>Mittagspause</td><td>Mittagspause</td></tr>
    <tr><td>15:30-16:00</td><td>Termin-<br>sprechstunde</td><td>Termin-<br>sprechstunde</td><td>Termin-<br>sprechstunde</td><td>Termin-<br>sprechstunde</td><td>Termin-<br>sprechstunde</td></tr>
    <tr><td>16:00-17:00</td><td>Freie<br>Sprechstunde</td><td>Freie<br>Sprechstunde</td><td></td><td>Freie<br>Sprechstunde</td><td></td></tr>
    <tr><td>17:00-18:00</td><td>Freie<br>Sprechstunde</td><td>Freie<br>Sprechstunde</td><td></td><td>Freie<br>Sprechstunde</td><td></td></tr>
  </table>
</section>

<div class="team-photo" role="img" aria-label="Freigestelltes Porträtfoto von Carla M. Weidner in blauer Bluse"></div>
<h2 class="team-title">TRIFF DAS TEAM</h2>
<div class="team-line"></div>
<div class="arrow prev"><svg width="10" height="12"><polyline points="7,1 2,6 7,11" fill="none" stroke="#fff" stroke-width="2"/></svg></div>
<div class="arrow next"><svg width="10" height="12"><polyline points="3,1 8,6 3,11" fill="none" stroke="#fff" stroke-width="2"/></svg></div>
<div class="member">
  <h3>Carla M. Weidner</h3>
  <div class="pos">CEO</div>
  <p>But I must explain to you how all this mistaken idea of denouncing pleasure and praising pain was born and I will give you a complete account of the system, and expound the actual teachings of the great explorer of the truth, the master-builder of human happiness.</p>
  <p>No one rejects, dislikes, or avoids pleasure itself, because it is pleasure, but because those who do not know how to pursue pleasure rationally encounter consequences that are extremely painful. Nor again is there anyone who loves or pursues or desires to obtain pain of itself, because it is pain, but because occasionally circumstances occur in which toil and pain can procure him some great pleasure. To take a trivial example, which of us ever undertakes laborious physical exercise, except to obtain some advantage from it.</p>
  <p>But who has any right to find fault with a man who chooses to enjoy a pleasure that has no annoying consequences, or one who avoids a pain that produces.</p>
</div>

<footer class="footer">
  <h2 style="left:110px">SCHNELLER KONTAKT</h2>
  <h2 style="left:692px">KONTAKT FORMULAR</h2>
  <div class="contact" style="left:111px;top:142px"><svg width="12" height="15"><path d="M6 1a5 5 0 0 1 5 5c0 4-5 8-5 8S1 10 1 6a5 5 0 0 1 5-5z" fill="#7c90c4"/><circle cx="6" cy="6" r="2" fill="#1a2a5c"/></svg>Am Lindenhof 14, 48712 Ahrental</div>
  <div class="contact" style="left:111px;top:167px"><svg width="13" height="11"><rect x="0" y="3" width="13" height="8" fill="#7c90c4"/><rect x="2" y="0" width="9" height="3" fill="#7c90c4"/></svg>048715530419</div>
  <div class="contact" style="left:380px;top:142px"><svg width="13" height="13"><path d="M2 1l3 0 1 3-2 1c1 2 2 3 4 4l1-2 3 1 0 3c-6 0-10-4-10-10z" fill="#7c90c4"/></svg>048715530410</div>
  <div class="contact" style="left:380px;top:167px"><svg width="14" height="10"><rect x=".5" y=".5" width="13" height="9" fill="none" stroke="#7c90c4"/><polyline points="1,1 7,6 13,1" fill="none" stroke="#7c90c4"/></svg>info@praxis-ahrental.de</div>
  <div class="contact" style="left:111px;top:207px">Copyright © 2019. Gemeinschaftspraxis Ahrental<span style="margin-left:24px">Datenschutz-Bestimmungen</span></div>
  <div class="contact" style="left:111px;top:233px">Alle Rechte vorbehalten.</div>
  <div class="field" style="left:612px;top:121px;width:233px">Name:</div>
  <div class="field" style="left:854px;top:121px;width:233px">Telefon:</div>
  <div class="field" style="left:612px;top:180px;width:475px">Email:</div>
  <div class="submit">EINREICHEN</div>
</footer>

</body>
</html>
```